Thoroughbred Racing Partnership needs web design

Crown of Laurels Partners is a management group who buys horses and races them on both the West and East coasts. The premise of the business is for an investment as little as $500, anyone can be a partner and own a percentage of a horse(s). This is a low cost way of getting involved in the exciting sport of Thoroughbred Racing, without shouldering the heavy financial responsibility. Our target market is mostly males 40+ but we want to include all target markets. We are looking for something very clean and professional, we want to give an image of success. Nothing overly "artsy." I have included the logo in which you can incorporate in the site. Also, the logo colors will be the colors of our "silks." The silks are what the jockey wears and will be an important marketing tool for COL. We would like a very prominent picture of a racehorse somewhere on the homepage, we want to make it clear that is a website for Horseracing partnerships.

On the top of the site, it should say "Crown of Laurels" (on the top)
and below that "Thoroughbred Racing Partnerships." (below that)

The main sections, which should be across the top are:

Home
About Us
Ownership
Stable Roster
News
Contact us

Some of these will have drop down menus.

An example of a competitor website that we like is: www.harrowfieldstable.example
An example of a competitor website that we don't like is: www.gallopmarket.example
Updates

Project Deadline Extended
Reason: We have a Board of Directors meeting on the 22nd and we will be making a decision on that day. I'm giving an extension so that all designers are able to submit their designs by the 22nd. Thank you!

Target Market(s)

40+ males

Industry/Entity Type

Business

Requirements
Must have
• our logo must be on the site. We would like at least one bold image of a thoroughbred horse in action. The picture is going to tell the story so it needs to be very eye-catching.

Our slogan should also be included on the website, "Experience the thrill of owning a Racehorse."
Should not have
• cartoons, artsy pictures, pictures of Steeplechase horses or "jumpers." This partnership is for racehorses only, there is not jumping involved with the horses.

```html
<!DOCTYPE html>
<html lang="en">
<head>
<meta charset="utf-8">
<title>Crown of Laurels Partners – Thoroughbred Racing Partnerships</title>
<link href="https://fonts.googleapis.com/css2?family=Oswald:wght@300;400&family=Open+Sans:ital,wght@0,400;0,600;0,700;1,400&display=swap" rel="stylesheet">
<style>
:root{
  --header-blue:#135a8e;
  --band-blue:#16598b;
  --navy:#0c1c4f;
  --footer-navy:#061848;
  --accent:#1a5f94;
  --link-blue:#4aa6e6;
  --page-grey:#e6e6e6;
  --text:#333;
  --white:#fff;
}
*{box-sizing:border-box;margin:0;padding:0}
html,body{width:1059px;height:1200px;overflow:hidden}
body{font-family:"Open Sans",sans-serif;color:var(--text);background:var(--page-grey);position:relative}

/* Header */
.site-header{position:absolute;left:0;top:0;width:1059px;height:103px;background:var(--header-blue);box-shadow:0 2px 4px rgba(0,0,0,.3);z-index:2}
.brand{position:absolute;left:126px;top:18px;display:flex;align-items:center;gap:8px}
.brand-mark{width:42px;height:42px;border-radius:50%;background:#dfe7ef}
.brand-name{font-weight:600;font-size:19px;color:#dfe7ef;line-height:1.15}
.tagline{position:absolute;left:687px;top:9px;font-style:italic;font-size:14.5px;line-height:22px;color:#dbe8f4}
.main-nav{position:absolute;left:398px;top:69px;display:flex;align-items:center}
.main-nav a{font-size:11.8px;font-weight:700;color:var(--white);text-decoration:none;padding:0 13px;line-height:24px;border-left:1px solid rgba(255,255,255,.18)}
.main-nav a:first-child{border-left:none}
.main-nav a.active{background:linear-gradient(#fff,#cfdde8);color:var(--navy);border-radius:3px;padding:0 8px;margin-right:6px}

/* Hero */
.hero{position:absolute;left:0;top:103px;width:1059px;height:457px;overflow:hidden}
.hero-photo{position:absolute;inset:0;background:linear-gradient(180deg,#b7bbbe 0%,#a2a8aa 22%,#7c848c 45%,#6f8a72 66%,#72a05a 84%,#6a9a4e 100%)}
.hero-slogan{position:absolute;left:640px;top:50px;font-family:"Oswald",sans-serif;font-weight:400;font-size:33px;line-height:36px;color:var(--white);text-shadow:0 1px 3px rgba(0,0,0,.3)}
.slider-dots{position:absolute;left:816px;top:431px;display:flex;gap:4px}
.slider-dots span{width:31px;height:7px;background:var(--navy)}
.slider-dots span.on{background:var(--white)}

/* Intro */
.intro{position:absolute;left:0;top:560px;width:1059px;height:194px;background:var(--band-blue)}
.intro h1{position:absolute;left:126px;top:12px;width:526px;font-family:"Oswald",sans-serif;font-weight:300;font-size:23px;color:var(--white);padding-bottom:5px;border-bottom:1px solid rgba(255,255,255,.35)}
.intro p{position:absolute;left:126px;top:61px;width:530px;font-size:11.6px;font-weight:600;line-height:18.5px;color:var(--white)}
.btn{display:inline-block;font-family:Arial,sans-serif;font-weight:700;font-size:10.5px;text-decoration:none;border-radius:3px;text-align:center}
.btn-light{background:linear-gradient(#fff,#d7e3ee);color:var(--accent)}
.btn-dark{background:var(--accent);color:var(--white)}
.intro .btn{position:absolute;left:566px;top:151px;width:79px;height:20px;line-height:20px}
.video{position:absolute;left:683px;top:12px;width:250px;height:170px;border:1px solid #fff;background:#1a1a1a}
.video-still{position:absolute;left:0;top:0;width:248px;height:143px;background:linear-gradient(90deg,#3c3232,#6b5a50 50%,#34324a)}
.play{position:absolute;left:102px;top:58px;width:40px;height:38px;background:#c8272a;border-radius:5px}
.video-bar{position:absolute;left:0;bottom:0;width:248px;height:25px;background:linear-gradient(#3a3a3a,#161616);color:#ccc;font-size:8.5px;line-height:25px;padding-left:82px}

/* Feature cards */
.card{position:absolute;top:778px;width:265px;height:246px;background:linear-gradient(#f7f7f5,#dcdcdc);border-radius:6px;box-shadow:0 3px 4px rgba(0,0,0,.18)}
.card-head{height:33px;background:var(--navy);border-radius:6px 6px 0 0;position:relative}
.card-head h2{position:absolute;left:64px;top:0;font-family:"Oswald",sans-serif;font-weight:400;font-size:23px;line-height:36px;color:var(--white)}
.card-icon{position:absolute;left:5px;top:-1px;width:49px;height:42px;border-radius:50%;background:var(--white);display:flex;align-items:center;justify-content:center}
.card-body{position:relative;padding:9px 9px 0}
.card-ownership{left:124px}
.card-testimonials{left:397px}
.card-contact{left:670px}
.card-ownership p{font-size:10.1px;line-height:16.2px;letter-spacing:-.15px;color:#333}
.checklist{list-style:none;margin-top:7px}
.checklist li{position:relative;padding-left:24px;font-size:10.4px;font-weight:700;color:var(--accent);line-height:18.5px}
.checklist svg{position:absolute;left:2px;top:4px}
.card .btn-dark{position:absolute;width:79px;height:19px;line-height:19px}
.card-ownership .btn-dark{left:169px;top:217px}
.card-testimonials .btn-dark{left:171px;top:218px}
.portrait{position:absolute;left:12px;top:54px;width:66px;height:70px;border:1px solid #bbb;background:linear-gradient(#9fb8cf,#4c5a6c)}
.quote{position:absolute;left:95px;top:54px;width:160px;font-size:10.4px;line-height:17.5px;color:#333}
.quote-mark{font-family:Georgia,serif;color:#999;font-size:14px;line-height:10px}
.quote-name{position:absolute;left:94px;top:147px;font-size:12px;font-weight:700;color:var(--accent)}
.quote-role{position:absolute;left:94px;top:168px;font-size:12px;font-weight:600;color:#333}
.field{position:absolute;left:9px;width:239px;height:22px;background:#fbfbf8;border:1px solid #ccc;font-size:10px;color:#444;padding:3px 8px}
.field-msg{height:62px}
.card-contact .btn-dark{left:169px;top:216px;width:79px;height:20px;line-height:20px}

/* Footer */
.site-footer{position:absolute;left:0;top:1046px;width:1059px;height:154px;background:var(--footer-navy);color:var(--white)}
.foot-col{position:absolute;top:14px}
.foot-divider{position:absolute;top:6px;width:1px;height:142px;background:rgba(255,255,255,.08)}
.foot-col h3{font-size:13.5px;font-weight:600;color:var(--link-blue);padding-bottom:2px;border-bottom:1px dashed rgba(255,255,255,.3);margin-bottom:10px}
.quick-links{left:126px;width:99px}
.quick-links ul{list-style:none;padding-left:8px}
.quick-links li{font-size:10.4px;line-height:15px}
.quick-links li.current{color:var(--link-blue)}
.newsletter{left:301px;width:166px}
.newsletter p{font-size:10.2px;line-height:12px;padding-left:3px}
.email-input{margin:12px 0 0 1px;width:147px;height:22px;background:var(--header-blue);border:1px solid #3c80b6;font-size:9px;font-style:italic;color:#9cc0de;padding:4px 5px}
.signup{display:block;margin:8px 0 0 76px;width:72px;height:20px;line-height:20px;background:linear-gradient(#fff,#c9d6e2);color:var(--navy);font-size:11.5px;font-weight:700;text-align:center;border-radius:2px}
.hq{left:543px;width:166px}
.hq p{font-size:10.4px;line-height:16px;padding-left:3px}
.hq .contact-line{display:flex;align-items:center;gap:8px;font-weight:700;margin-top:4px}
.foot-brand{left:792px;top:20px;width:140px}
.foot-brand .brand-name{font-size:15px;text-align:center}
.socials{display:flex;gap:9px;justify-content:center;margin-top:30px}
.socials span{width:24px;height:24px;border-radius:50%;background:#2c6aa8}
.copyright{font-size:8px;text-align:center;margin-top:14px}
</style>
</head>
<body>

<header class="site-header">
  <div class="brand">
    <span class="brand-mark"></span>
    <span class="brand-name">COL<br>PARTNERS.COM</span>
  </div>
  <div class="tagline">Crown of Laurels<br>Thoroughbred Racing Partnerships.</div>
  <nav class="main-nav">
    <a href="#" class="active">HOME</a>
    <a href="#">ABOUT US</a>
    <a href="#">OWNERSHIP</a>
    <a href="#">STABLE ROSTER</a>
    <a href="#">NEWS</a>
    <a href="#">CONTACT US</a>
  </nav>
</header>

<section class="hero">
  <div class="hero-photo" role="img" aria-label="Jockey in blue silks celebrating on a grey thoroughbred racehorse, green turf behind"></div>
  <div class="hero-slogan">Experience the thrill of<br>owning a Racehorse</div>
  <div class="slider-dots"><span class="on"></span><span></span><span></span></div>
</section>

<section class="intro">
  <h1>Crown of Laurels Thoroughbred Partnerships</h1>
  <p>Crown of Laurels Partners is a management group who buys horses and races them on both the West and East coasts. The premise of the business is for an investment as little as $500, anyone can be a partner and own a percentage of a horse(s). This is a low cost way of getting involved in the exciting sport of Thoroughbred Racing, without shouldering the heavy financial responsibility.</p>
  <a href="#" class="btn btn-light">Read more »</a>
  <div class="video">
    <div class="video-still" role="img" aria-label="Video still of three partners holding an award plaque"></div>
    <svg class="play" viewBox="0 0 40 38"><polygon points="15,10 29,19 15,28" fill="#fff"/></svg>
    <div class="video-bar">0:00 / 0:00</div>
  </div>
</section>

<article class="card card-ownership">
  <div class="card-head">
    <span class="card-icon"><svg width="26" height="16" viewBox="0 0 26 16"><ellipse cx="13" cy="8" rx="11" ry="5" fill="none" stroke="#1a5f94" stroke-width="2.5"/></svg></span>
    <h2>Ownership Pride</h2>
  </div>
  <div class="card-body">
    <p>Lorem ipsum dolor sit amet, consectet adipiscing elit, sed diam nonummy nibh euismod tincidunt ut laoreet dolore magna aliquam erat volutpat.Ut wisi enim ad minim veniam, quis nostru exe ullamcorper suscipit lobortis nisl ut aliquip commod consequat.</p>
    <ul class="checklist">
      <li><svg width="14" height="12"><path d="M1 6 L5 11 L13 1" fill="none" stroke="#1a5f94" stroke-width="1.5"/></svg>Lorem ipsum dolor sit amet</li>
      <li><svg width="14" height="12"><path d="M1 6 L5 11 L13 1" fill="none" stroke="#1a5f94" stroke-width="1.5"/></svg>Sed diam nonummy nibh euismod</li>
      <li><svg width="14" height="12"><path d="M1 6 L5 11 L13 1" fill="none" stroke="#1a5f94" stroke-width="1.5"/></svg>Ut wisi enim ad minim</li>
      <li><svg width="14" height="12"><path d="M1 6 L5 11 L13 1" fill="none" stroke="#1a5f94" stroke-width="1.5"/></svg>Consectet adipiscing elit</li>
    </ul>
  </div>
  <a href="#" class="btn btn-dark">Read more »</a>
</article>

<article class="card card-testimonials">
  <div class="card-head">
    <span class="card-icon"><svg width="28" height="24" viewBox="0 0 28 24"><rect x="1" y="2" width="18" height="12" rx="3" fill="#0c1c4f"/><rect x="9" y="9" width="18" height="11" rx="3" fill="#1a5f94"/><polygon points="20,20 25,20 24,24" fill="#1a5f94"/></svg></span>
    <h2>Client Testimonials</h2>
  </div>
  <div class="portrait" role="img" aria-label="Portrait photo of a smiling executive"></div>
  <p class="quote"><span class="quote-mark">“</span> Ut wisi enim ad mini veniam, quis nostrud exerci tationullamo corper suscipit lobortis nislutalil uip  ullamcorper suscipit lobortis aliquip commod consequat.</p>
  <div class="quote-name">Mr. Lorem ipsum sit amet</div>
  <div class="quote-role">Chief Executive</div>
  <a href="#" class="btn btn-dark">Read more »</a>
</article>

<article class="card card-contact">
  <div class="card-head">
    <span class="card-icon"><svg width="20" height="24" viewBox="0 0 20 24"><path d="M2 1 H13 L18 6 V23 H2 Z" fill="none" stroke="#1a5f94" stroke-width="2"/><path d="M6 17 L13 9" stroke="#1a5f94" stroke-width="2.5"/></svg></span>
    <h2>Quick Contact</h2>
  </div>
  <div class="field" style="top:50px">Your Name</div>
  <div class="field" style="top:78px">Email</div>
  <div class="field" style="top:107px">Phone</div>
  <div class="field field-msg" style="top:137px">Message</div>
  <a href="#" class="btn btn-dark">Submit</a>
</article>

<footer class="site-footer">
  <div class="foot-col quick-links">
    <h3>Quick Links</h3>
    <ul>
      <li class="current">Home</li><li>About Us</li><li>Ownership</li><li>Stable Roster</li><li>News</li><li>Contact us</li>
    </ul>
  </div>
  <span class="foot-divider" style="left:264px"></span>
  <div class="foot-col newsletter">
    <h3>Newsletter Signup</h3>
    <p>Signup with us and get news and update in your inbox</p>
    <div class="email-input">Email here</div>
    <span class="signup">Signup</span>
  </div>
  <span class="foot-divider" style="left:505px"></span>
  <div class="foot-col hq">
    <h3>Company Headquarter</h3>
    <p>Lorem ipsum dolor sit amet<br>consectetuer adipsi<br>Po Box-7314</p>
    <p class="contact-line"><svg width="12" height="12" viewBox="0 0 12 12"><path d="M2 1 L4 1 L5 4 L3.5 5 Q5 8 7 8.5 L8 7 L11 8 L11 10 Q6 12 2 6 Q0.5 3 2 1Z" fill="#4aa6e6"/></svg>001 5550-20418</p>
    <p class="contact-line"><svg width="14" height="10" viewBox="0 0 14 10"><rect x="0.5" y="0.5" width="13" height="9" fill="none" stroke="#4aa6e6"/><path d="M0.5 0.5 L7 6 L13.5 0.5" fill="none" stroke="#4aa6e6"/></svg>info@colpartners.example</p>
  </div>
  <span class="foot-divider" style="left:746px"></span>
  <div class="foot-col foot-brand">
    <div class="brand-name">COL<br>PARTNERS.COM</div>
    <div class="socials"><span></span><span></span><span></span><span></span></div>
    <p class="copyright">© 2013 Crown of Laurels Partners</p>
  </div>
</footer>

</body>
</html>
```